Proposal Brochure for Shopfitting / Construction company

We require a proposal document (Business Capabilities) to give to customers who we are tendering to, to tell them about our business. We are a shopfitting company who complete design, fit out, project management and joinery manufacture. Please see our website www.halvenfit.com.au and use information in that. The document needs to be editable so that we can add to it. An editable template would be great. You can use a mix of our photos and stock photos if you like. Please use our logo colours. Orange, gray, black white so that it all ties in. We use Publisher and Powerpoint.

Target Market(s)

Commerical Builders, Retailers, Business

Industry/Entity Type

Construction Company

Font styles to use
Sans Serif

Colors
f37122
f68d4d
333333
5c5c5c
9d9d9d

Requirements
Must have
• Must have logo, relevant photos, use logo colours Orange, black, gray. Can you stock photos or Ones provided. Business Proposal document, about us, capabiities, services etc. Use content from our website
Nice to have
• Template to be editable

```html
<!DOCTYPE html>
<html lang="en">
<head>
<meta charset="utf-8">
<title>Halvenfit Australia – Capabilities Brochure Cover</title>
<link href="https://fonts.googleapis.com/css2?family=Oswald:wght@300;600&family=Montserrat:wght@400;500&display=swap" rel="stylesheet">
<style>
  :root {
    --orange: #f37122;
    --orange-light: #f68d4d;
    --charcoal: #333333;
    --slate: #3a3f47;
    --grey-mid: #5c5c5c;
    --grey-light: #9d9d9d;
    --paper: #f4f4f2;
    --backdrop: #c9c9c9;
    --white: #ffffff;
  }
  * { margin: 0; padding: 0; box-sizing: border-box; }
  html, body {
    width: 1200px;
    height: 804px;
    overflow: hidden;
    background: var(--backdrop);
  }
  .stage {
    position: relative;
    width: 1200px;
    height: 804px;
    display: flex;
    align-items: center;
    justify-content: center;
  }
  .cover {
    position: relative;
    width: 523px;
    height: 740px;
    background: var(--paper);
    overflow: hidden;
    box-shadow: 0 6px 18px rgba(0,0,0,0.18);
  }
  .cover-art {
    position: absolute;
    inset: 0;
    width: 100%;
    height: 100%;
  }
  .store-photo {
    position: absolute;
    left: 0;
    top: 0;
    width: 523px;
    height: 640px;
    background:
      linear-gradient(160deg, #6f9a2e 0%, #7fa637 14%, rgba(216,194,160,0) 30%),
      radial-gradient(ellipse at 55% 35%, #e8d9bd 0%, rgba(232,217,189,0) 45%),
      linear-gradient(180deg, #d8c7a7 0%, #a0744a 45%, #6b4a32 70%, #8a6a4a 100%);
  }
  .title {
    position: absolute;
    left: 292px;
    top: 432px;
    color: var(--white);
    font-family: "Oswald", sans-serif;
    text-transform: uppercase;
    line-height: 1;
  }
  .title-light {
    display: block;
    font-weight: 300;
    font-size: 40px;
    letter-spacing: 0.5px;
  }
  .title-bold {
    display: block;
    font-weight: 600;
    font-size: 44px;
    margin-top: 4px;
    letter-spacing: 0.5px;
  }
  .tagline {
    position: absolute;
    left: 268px;
    top: 560px;
    color: var(--white);
    font-family: "Montserrat", sans-serif;
    font-size: 11.5px;
    letter-spacing: 0.8px;
    text-transform: uppercase;
  }
  .web-address {
    position: absolute;
    right: 26px;
    top: 654px;
    color: var(--grey-mid);
    font-family: "Montserrat", sans-serif;
    font-size: 10px;
    letter-spacing: 2px;
  }
  .brand {
    position: absolute;
    left: 30px;
    bottom: 34px;
    display: flex;
    align-items: center;
    gap: 12px;
  }
  .brand-mark {
    width: 34px;
    height: 34px;
    background: var(--orange);
  }
  .brand-name {
    font-family: "Montserrat", sans-serif;
    font-weight: 500;
    font-size: 17px;
    letter-spacing: 2px;
    text-transform: uppercase;
    color: var(--charcoal);
  }
</style>
</head>
<body>
<main class="stage">
  <section class="cover">
    <div class="store-photo" role="img" aria-label="Photograph of a fitted-out retail footwear store with green ceiling bulkhead, shoe display walls, island fixtures and round green ottomans"></div>
    <svg class="cover-art" viewBox="0 0 523 740" aria-hidden="true">
      <polygon class="band-slate" points="0,430 170,513 0,640" fill="var(--slate)"/>
      <polygon class="band-orange" points="0,640 523,250 523,640" fill="var(--orange)"/>
      <rect class="footer-strip" x="0" y="640" width="523" height="100" fill="var(--paper)"/>
    </svg>
    <h1 class="title">
      <span class="title-light">Halvenfit</span>
      <span class="title-bold">Australia</span>
    </h1>
    <p class="tagline">Inspired . Creative . Functional</p>
    <p class="web-address">www.halvenfit.com.au</p>
    <div class="brand">
      <span class="brand-mark"></span>
      <span class="brand-name">Halvenfit Australia</span>
    </div>
  </section>
</main>
</body>
</html>
```